依頼詳細
■地域系LP(PC・スマホサイト)
ページ数:各1ページづつ作成
ワイヤーフレーム:あり
https://pelvix.com/diagrams/RaqM8WbNpe4kV2sY#913KD

※メイン画像部分は写真を入れ込んでデザインお願いします。
(それ以外の素材は支給頂ける予定)
※有料画像を使用する場合は画像の費用は自己負担でお願いします。
※PC、スマホ版ともにデザインの方向性は合わせてください。
※スマホ版は幅640pxで作成お願いします。

■デザイン参考サイト
https://mosuplint.jp/
https://mosuplint.jp/lp/sp/300aa/00/00/00/

■コーディング
一切不要。

■ページ数
PC1ページ
スマホ1ページ
■納品
画像データと制作ファイルを納品ください。
(それ以外の素材は支給頂ける予定)
※スマホ版は幅640pxで作成お願いします。
■ 選んだ理由

情報の伝わりやすいさ、すっきりとしたデザインを評価させていただきました。

■ 提案者全員のお礼・コメント

ご応募くださり、ありがとうございます。
また次回のデザインコンペにもご参加いただけますと幸いです。
よろしくお願いいたします。

```html
<!DOCTYPE html>
<html lang="ja">
<head>
<meta charset="utf-8">
<title>モスプリント 東京 就職カウンセリング</title>
<link href="https://fonts.googleapis.com/css2?family=Noto+Sans+JP:wght@400;500;700;900&family=Noto+Serif+JP:wght@500;700&display=swap" rel="stylesheet">
<style>
:root{
  --green:#8cc63f;
  --blue:#2f8fd3;
  --blue-dark:#1d6fb0;
  --sky:#e6f2fb;
  --sky-mid:#4ea6e0;
  --orange:#f39800;
  --orange-dark:#e07d00;
  --ink:#333;
  --muted:#777;
  --line:#d8d8d8;
  --beige:#f5efe2;
  --brown:#7a5a3a;
  --white:#fff;
}
*{box-sizing:border-box;margin:0;padding:0}
html,body{width:1200px;height:4180px;overflow:hidden}
body{font-family:"Noto Sans JP",sans-serif;color:var(--ink);background:var(--white);font-size:14px;line-height:1.7}
.wordmark{font-weight:900;color:var(--green);letter-spacing:2px;display:flex;align-items:center;gap:10px}
.wordmark i{display:block;width:18px;height:18px;background:var(--green);border-radius:50%}

/* header */
.site-header{height:80px;display:flex;align-items:center;justify-content:space-between;padding:0 110px 0 130px}
.site-header .wordmark{font-size:30px}
.header-cta{background:var(--orange);color:#fff;font-weight:700;font-size:14px;padding:10px 26px;border-radius:4px}

/* hero */
.hero{height:370px;background:linear-gradient(180deg,#cfe7f7,#eaf5fc);position:relative;overflow:hidden}
.hero-copy{position:absolute;left:130px;top:22px;width:640px}
.hero-lead{background:var(--blue);color:#fff;font-weight:900;font-size:30px;padding:2px 18px;display:inline-block}
.hero-title{background:#fff;margin-top:10px;padding:6px 20px 10px;font-weight:900;font-size:46px;line-height:1.35;color:#1c3d63;display:inline-block}
.hero-title span{color:var(--blue)}
.hero-stats{position:absolute;left:130px;top:268px;display:flex;gap:18px}
.stat{width:190px;height:84px;background:#fff;border:2px solid var(--blue);text-align:center}
.stat-label{background:var(--blue);color:#fff;font-size:14px;font-weight:700;line-height:24px}
.stat-value{font-size:34px;font-weight:900;color:var(--orange);line-height:1.4}
.stat-value small{font-size:16px;color:var(--ink)}
.hero-photo{position:absolute;right:110px;top:0;width:380px;height:370px;background:linear-gradient(180deg,#d9e6ef,#b8c9d6)}
.hero-badge{position:absolute;right:150px;top:250px;background:var(--blue);color:#fff;font-weight:700;font-size:15px;padding:10px 18px;line-height:1.5}

/* support strip */
.support{height:50px;display:flex;align-items:center;justify-content:center;border-bottom:3px solid var(--blue);font-weight:700;font-size:20px}

/* cta */
.cta{height:290px;background:var(--sky);display:flex;align-items:center;justify-content:center}
.cta-box{width:940px;height:210px;background:var(--sky-mid);padding:26px 40px;color:#fff}
.cta-box h2{font-size:22px;font-weight:700;margin-bottom:18px}
.cta-row{display:flex;gap:20px;align-items:center}
.tel{width:380px;height:90px;background:var(--blue-dark);padding:10px 20px}
.tel small{font-size:12px;display:block}
.tel strong{font-size:34px;font-weight:900;display:flex;align-items:center;gap:10px;line-height:1.3}
.cta-button{width:380px;height:90px;background:var(--orange);display:flex;align-items:center;justify-content:center;font-size:22px;font-weight:700;border-radius:4px;box-shadow:0 4px 0 var(--orange-dark)}

/* rate */
.rate{height:230px;display:flex;flex-direction:column;align-items:center;justify-content:center;gap:10px}
.rate .wordmark{font-size:48px}
.rate p{font-family:"Noto Serif JP",serif;font-size:30px;font-weight:500}
.rate p em{font-style:normal;color:var(--orange);font-size:56px;font-weight:700}

/* voice */
.voice-banner{height:90px;background:repeating-linear-gradient(45deg,var(--blue) 0 12px,#3a98d9 12px 24px);display:flex;align-items:center;justify-content:center}
.voice-banner p{background:#fff;padding:8px 40px;font-weight:700;font-size:20px}
.voice{height:830px;background:var(--sky);display:flex;justify-content:center;gap:40px;padding-top:60px}
.voice-card{width:430px;height:700px;background:#fff;border:1px solid var(--line)}
.voice-photo{height:280px;background:linear-gradient(180deg,#c9b8a8,#8c7b6d)}
.voice-card:nth-child(2) .voice-photo{background:linear-gradient(180deg,#c4c9cf,#6b7480)}
.voice-head{display:flex;justify-content:space-between;align-items:center;padding:16px 26px;border-bottom:1px dashed var(--line)}
.voice-head b{font-size:22px;color:var(--blue)}
.voice-head b small{font-size:13px;color:var(--ink);font-weight:400}
.voice-head span{background:var(--blue);color:#fff;font-size:13px;padding:2px 10px}
.voice-head span em{font-style:normal;color:#ffd24d;font-weight:700}
.voice-card p{padding:16px 26px;font-size:13px;line-height:1.95}

/* form */
.form-title{height:60px;background:var(--orange);color:#fff;font-weight:700;font-size:22px;display:flex;align-items:center;padding-left:170px;margin-top:20px}
.apply{height:1110px;padding:50px 0 0 200px}
.row{display:flex;align-items:center;margin-bottom:22px}
.row label{width:140px;text-align:right;padding-right:24px;font-size:13px}
.row label i{font-style:normal;background:#e05a4d;color:#fff;font-size:10px;padding:1px 5px;margin-left:6px}
.field{height:34px;border:1px solid #bbb;background:#fff;font-size:12px;color:#aaa;padding:6px 10px}
.w230{width:230px}.w120{width:120px;margin-right:12px}.w330{width:330px}.w400{width:400px}
.pair{display:flex;gap:14px}
.radio{display:flex;gap:24px;font-size:13px;align-items:center}
.radio span::before{content:"";display:inline-block;width:13px;height:13px;border:1px solid #999;border-radius:50%;margin-right:6px;vertical-align:-2px}
.hint{font-size:11px;color:var(--muted);margin-left:14px}
.area{width:560px;height:120px}
.consent{text-align:center;margin:50px 0 0 -200px;font-size:12px}
.consent p{color:var(--muted);font-size:11px}
.submit{margin:22px auto 0;width:230px;height:44px;background:var(--orange);color:#fff;font-weight:700;font-size:14px;display:flex;align-items:center;justify-content:center;border-radius:4px}

/* access */
.access{height:930px;background:var(--beige);padding:50px 0 0}
.access h2{width:940px;margin:0 auto;border-top:1px solid var(--brown);border-bottom:1px solid var(--brown);font-size:22px;font-weight:700;padding:6px 0;color:var(--brown);text-align:center;font-family:"Noto Serif JP",serif}
.access>p{width:940px;margin:18px auto;font-size:12px;color:var(--ink)}
.map-card{width:940px;margin:0 auto 30px;background:#fff;border:1px solid var(--line)}
.map-card h3{background:var(--brown);color:#fff;font-size:14px;font-weight:700;padding:6px 16px}
.map-body{height:270px;position:relative;margin:14px;background:linear-gradient(135deg,#ece6d8,#e3dfd4)}
.map-info{position:absolute;left:20px;top:20px;width:250px;background:#fff;border:1px solid var(--line);padding:10px 14px;font-size:11px;line-height:1.7}
.map-info b{font-size:12px}
.pin{position:absolute;left:470px;top:100px}

/* footer */
.site-footer{height:100px;display:flex;align-items:center;justify-content:space-between;padding:0 130px;border-top:1px solid var(--line)}
.site-footer .brand{font-weight:700;font-size:24px;color:#1c3d63}
.site-footer small{display:block;font-size:10px;color:var(--muted)}
.footer-mark{width:38px;height:38px;border:2px solid var(--blue);border-radius:50%}
</style>
</head>
<body>

<header class="site-header">
  <div class="wordmark"><i></i>モスプリント</div>
  <div class="header-cta">まずは相談してみる</div>
</header>

<section class="hero">
  <div class="hero-copy">
    <div class="hero-lead">東京で正社員求人をお探しの</div><br>
    <div class="hero-title">20代のフリーター・既卒<br><span>未経験から</span>正社員へ</div>
  </div>
  <div class="hero-stats">
    <div class="stat"><div class="stat-label">サービス利用者</div><div class="stat-value">34,042<small>人</small></div></div>
    <div class="stat"><div class="stat-label">紹介企業数</div><div class="stat-value">1,000<small>社</small></div></div>
    <div class="stat"><div class="stat-label">内定率</div><div class="stat-value">78.7<small>%</small></div></div>
  </div>
  <div class="hero-photo" role="img" aria-label="笑顔のキャリアカウンセラーの写真"></div>
  <div class="hero-badge">あなたにぴったりな<br>求人をご紹介<br>担当カウンセリング</div>
</section>

<div class="support">あなた専属のコンサルタントが東京都での就職活動を徹底サポート</div>

<section class="cta">
  <div class="cta-box">
    <h2>東京都で就職カウンセリングを受けるなら</h2>
    <div class="cta-row">
      <div class="tel">
        <small>お電話でのお問い合わせ</small>
        <strong><svg width="34" height="24" viewBox="0 0 34 24"><rect x="1" y="3" width="32" height="18" rx="4" fill="#fff"/><text x="17" y="17" text-anchor="middle" font-size="12" font-weight="700" fill="#1d6fb0">FREE</text></svg>0120-000-000</strong>
        <small>受付時間 平日 9:00〜20:00</small>
      </div>
      <div class="cta-button">無料カウンセリングお申し込み</div>
    </div>
  </div>
</section>

<section class="rate">
  <div class="wordmark"><i></i>モスプリント</div>
  <p>就職内定率<em>78</em>%以上</p>
</section>

<div class="voice-banner"><p>「モスプリント」を利用して就職された方から多くの満足の声をいただいております!</p></div>
<section class="voice">
  <article class="voice-card">
    <div class="voice-photo" role="img" aria-label="利用者の女性の写真"></div>
    <div class="voice-head"><b>M.Sさん<small>(女性 / 24歳)</small></b><span>年収 <em>約320万円</em></span></div>
    <p>短大卒業後はアルバイトを続けていましたが、将来が不安になり相談しました。担当の方が私の希望をじっくり聞いてくださり、未経験でも挑戦できる事務職の求人を紹介していただきました。面接対策では話し方や志望動機の作り方まで丁寧に教えてもらい、自信を持って選考に臨むことができました。初めての正社員で不安もありましたが、入社後も気軽に相談できる環境があり、今では毎日楽しく働いています。一人で悩まずに相談して本当によかったと思います。</p>
  </article>
  <article class="voice-card">
    <div class="voice-photo" role="img" aria-label="利用者の男性の写真"></div>
    <div class="voice-head"><b>S.Iさん<small>(男性 / 26歳)</small></b><span>年収 <em>約350万円</em></span></div>
    <p>大学卒業後に就職せず、フリーターとして数年過ごしていました。自分に何ができるのか分からないまま相談に行きましたが、これまでの経験から強みを一緒に見つけていただきました。営業職の求人を複数紹介してもらい、企業ごとの特徴も詳しく説明してもらえたので安心して選べました。選考の日程調整もすべて任せられたため、準備に集中することができました。今は目標を持って仕事に取り組めており、あのとき一歩踏み出して本当によかったです。</p>
  </article>
</section>

<div class="form-title">無料カウンセリングのお申し込み</div>
<section class="apply">
  <div class="row"><label>お名前<i>必須</i></label><div class="pair"><div class="field w230">姓</div><div class="field w230">名</div></div></div>
  <div class="row"><label>お名前(ふりがな)<i>必須</i></label><div class="pair"><div class="field w230">せい</div><div class="field w230">めい</div></div></div>
  <div class="row"><label>性別<i>必須</i></label><div class="radio"><span>男性</span><span>女性</span></div></div>
  <div class="row"><label>生年月日<i>必須</i></label><div class="field w120">1990年</div><div class="field w120">1月</div><div class="field w120">1日</div></div>
  <div class="row"><label>都道府県<i>必須</i></label><div class="field w230">東京都</div></div>
  <div class="row"><label>最終学歴<i>必須</i></label><div class="field w330">選択してください</div></div>
  <div class="row"><label>電話番号<i>必須</i></label><div class="field w330">例)09012345678</div></div>
  <div class="row"><label>メールアドレス<i>必須</i></label><div class="field w400">例)info@example.jp</div><span class="hint">確認メールが届きます</span></div>
  <div class="row" style="align-items:flex-start"><label>ご質問</label><div class="field area"></div></div>
  <div class="consent">
    <div>こちらをご確認の上 <u>個人情報の取扱い</u> に同意してください</div>
    <p>ご入力いただいた情報はカウンセリングのご案内のみに利用し、第三者に提供することはありません。</p>
    <div class="submit">上記に同意して送信する</div>
  </div>
</section>

<section class="access">
  <h2>アクセスマップ</h2>
  <p>モスプリントの就職カウンセリングは都内2拠点にて実施しております。ご希望の拠点をお選びいただき、お気軽にお越しください。当日は担当カウンセラーがお迎えいたします。</p>
  <div class="map-card">
    <h3>新宿拠点のマップ</h3>
    <div class="map-body" role="img" aria-label="新宿拠点周辺の地図">
      <div class="map-info"><b>新宿カウンセリングルーム</b><br>東京都新宿区西新宿1丁目 サンプルビル5F<br>新宿駅 西口より徒歩5分</div>
      <svg class="pin" width="30" height="40" viewBox="0 0 30 40"><path d="M15 1C7 1 1 7 1 15c0 10 14 24 14 24s14-14 14-24C29 7 23 1 15 1z" fill="#e05a4d"/><circle cx="15" cy="15" r="5" fill="#fff"/></svg>
    </div>
  </div>
  <div class="map-card">
    <h3>渋谷拠点のマップ</h3>
    <div class="map-body" role="img" aria-label="渋谷拠点周辺の地図">
      <div class="map-info"><b>渋谷カウンセリングルーム</b><br>東京都渋谷区渋谷2丁目 サンプルタワー12F<br>渋谷駅 東口より徒歩3分</div>
      <svg class="pin" width="30" height="40" viewBox="0 0 30 40"><path d="M15 1C7 1 1 7 1 15c0 10 14 24 14 24s14-14 14-24C29 7 23 1 15 1z" fill="#e05a4d"/><circle cx="15" cy="15" r="5" fill="#fff"/></svg>
    </div>
  </div>
</section>

<footer class="site-footer">
  <div><div class="brand">Norvella</div><small>Copyright © Norvella Co., Ltd. All Rights Reserved.</small></div>
  <div class="footer-mark"></div>
</footer>

</body>
</html>
```